Billboard for a Contractor in Minnesota

Creating our first billboard that will be displayed on a freeway. Will be used on a digital Glint Signboard. Sign should be a 846 x 234 design. Our website is kestrel-paving.com Looking for something specific to "Look us up" or "Call" for your free concrete & asphalt estimate. Needs both web addresses (kestrel-paving.com and kestrel-masonry.com. Needs our phone number, logo. Our slogan is Serving All Your Asphalt & Concrete Needs. It's also our 25 Anniversary.

Target Market(s)

Residential Homeowners in the Twin Cities

Colors
abd036

Requirements
Must have
• Logo, Phone Number, Our Services, Web Addresses (both) Our services are all on our website. (Asphalt Driveway, Concrete Driveway, Concrete Apron, Concrete Sidewalk, Concrete Patio. Colors should be same as website. Black, White, Gray and the Neon Green color.

```html
<!DOCTYPE html>
<html lang="en">
<head>
<meta charset="utf-8">
<title>Kestrel Billboard</title>
<link rel="stylesheet" href="https://fonts.googleapis.com/css2?family=Montserrat:ital,wght@0,500;0,700;0,800;1,500&display=swap">
<style>
  :root {
    --page: #a9a9a9;
    --white: #ffffff;
    --black: #0b0b0b;
    --green: #56d14e;
    --photo-green: #7f9a68;
    --photo-gray: #c9ccc9;
    --badge: #2e8a6e;
  }
  * { box-sizing: border-box; margin: 0; padding: 0; }
  html, body { width: 1200px; height: 1000px; overflow: hidden; }
  body {
    background: var(--page);
    font-family: "Montserrat", Arial, sans-serif;
    position: relative;
  }
  .billboard {
    position: absolute;
    left: 58px; top: 350px;
    width: 1085px; height: 300px;
    background: var(--white);
    overflow: hidden;
    box-shadow: 0 14px 18px rgba(0,0,0,0.35);
  }
  .hero-photo {
    position: absolute;
    left: 0; top: 0;
    width: 500px; height: 260px;
    background: linear-gradient(90deg, var(--photo-green) 0%, var(--photo-gray) 45%, rgba(255,255,255,0.9) 80%, var(--white) 100%);
  }
  .brand {
    position: absolute;
    left: 50px; top: 150px;
    width: 320px;
    display: flex; align-items: center; gap: 14px;
  }
  .brand-dot {
    width: 34px; height: 34px; border-radius: 50%;
    background: var(--black);
    flex: none;
  }
  .brand-name {
    font-weight: 800;
    font-size: 52px;
    letter-spacing: 3px;
    color: var(--black);
  }
  .anniversary-badge {
    position: absolute;
    left: 367px; top: 178px;
    width: 76px; height: 76px;
    border-radius: 50%;
    background: var(--badge);
    border: 4px solid #8c8c8c;
  }
  .tagline {
    position: absolute;
    left: 440px; top: 18px; width: 600px;
    text-align: center;
    font-style: italic; font-weight: 500;
    font-size: 21px;
    color: var(--black);
  }
  .services {
    position: absolute;
    left: 405px; top: 55px; width: 680px;
    list-style: none;
    display: flex; flex-wrap: wrap; justify-content: center;
    column-gap: 14px; row-gap: 4px;
  }
  .service {
    display: flex; align-items: center; gap: 4px;
    font-weight: 800; font-size: 23px;
    color: var(--black);
    line-height: 30px;
  }
  .service svg { width: 16px; height: 16px; }
  .divider {
    position: absolute;
    left: 547px; top: 161px;
    width: 370px; height: 2px;
    background: var(--black);
  }
  .call-line {
    position: absolute;
    left: 447px; top: 172px;
    font-weight: 800; font-size: 33px;
    white-space: nowrap;
  }
  .call-line .cta { color: var(--green); }
  .call-line .phone { color: var(--black); margin-left: 6px; }
  .web-pill {
    position: absolute;
    left: 492px; top: 218px;
    width: 495px; height: 25px;
    border-radius: 13px;
    background: var(--green);
    text-align: center;
    font-weight: 700; font-size: 15px; line-height: 25px;
    color: var(--black);
  }
  .estimate-bar {
    position: absolute;
    left: 0; bottom: 0;
    width: 100%; height: 40px;
    background: var(--black);
    text-align: center;
    font-size: 23px; line-height: 40px;
    color: var(--green);
    font-weight: 500;
  }
  .estimate-bar strong { font-weight: 800; }
</style>
</head>
<body>
  <div class="billboard">
    <div class="hero-photo" role="img" aria-label="Photo of a suburban house with a freshly paved driveway and lawn"></div>

    <div class="brand">
      <span class="brand-dot"></span>
      <span class="brand-name">KESTREL</span>
    </div>
    <div class="anniversary-badge" role="img" aria-label="25th anniversary badge"></div>

    <p class="tagline">Serving All Your Asphalt &amp; Concrete Needs</p>

    <ul class="services">
      <li class="service"><svg viewBox="0 0 16 16"><rect x="1" y="3" width="12" height="12" fill="none" stroke="#0b0b0b" stroke-width="1.5"/><path d="M3.5 8.5l3 3L15 2" fill="none" stroke="#0b0b0b" stroke-width="2"/></svg>ASPHALT DRIVEWAY</li>
      <li class="service"><svg viewBox="0 0 16 16"><rect x="1" y="3" width="12" height="12" fill="none" stroke="#0b0b0b" stroke-width="1.5"/><path d="M3.5 8.5l3 3L15 2" fill="none" stroke="#0b0b0b" stroke-width="2"/></svg>CONCRETE DRIVEWAY</li>
      <li class="service"><svg viewBox="0 0 16 16"><rect x="1" y="3" width="12" height="12" fill="none" stroke="#0b0b0b" stroke-width="1.5"/><path d="M3.5 8.5l3 3L15 2" fill="none" stroke="#0b0b0b" stroke-width="2"/></svg>CONCRETE APRON</li>
      <li class="service"><svg viewBox="0 0 16 16"><rect x="1" y="3" width="12" height="12" fill="none" stroke="#0b0b0b" stroke-width="1.5"/><path d="M3.5 8.5l3 3L15 2" fill="none" stroke="#0b0b0b" stroke-width="2"/></svg>CONCRETE SIDEWALK</li>
      <li class="service"><svg viewBox="0 0 16 16"><rect x="1" y="3" width="12" height="12" fill="none" stroke="#0b0b0b" stroke-width="1.5"/><path d="M3.5 8.5l3 3L15 2" fill="none" stroke="#0b0b0b" stroke-width="2"/></svg>CONCRETE PATIO</li>
    </ul>

    <div class="divider"></div>

    <p class="call-line"><span class="cta">CALL US TODAY!</span><span class="phone">612-555-0148</span></p>

    <p class="web-pill">www.kestrel-paving.com / www.kestrel-masonry.com</p>

    <p class="estimate-bar">CALL US FOR YOUR <strong>FREE CONCRETE &amp; ASPHALT ESTIMATE</strong></p>
  </div>
</body>
</html>
```